KGLA-Postcard

We need a postcard design of a book. The card will be mailed out by Orbel Cards to church leaders. Attached, please find a photo of the book cover, Word doc. with the message that should placed on the card, and a pre-designed sample. You may use a similar layout as the PDF sample or something more attractive. If you can, copy the publisher's logo and book information from the PDF file. Thank you.

Church

```html
<!DOCTYPE html>
<html lang="en">
<head>
<meta charset="utf-8">
<title>KGLA Postcard</title>
<link href="https://fonts.googleapis.com/css2?family=Questrial&family=PT+Sans:ital,wght@0,400;0,700;1,700&family=Arimo:wght@700&family=Crimson+Text&display=swap" rel="stylesheet">
<style>
  :root {
    --paper: #ffffff;
    --ink: #111111;
    --night: #000000;
    --rule: #1a1a1a;
    --accent-red: #e0222a;
    --headline-grey: #555555;
    --title-white: #f2f2f2;
    --author-grey: #dcdcdc;
    --skin: #6a4a38;
    --earth: #2d5a86;
  }
  * { box-sizing: border-box; margin: 0; padding: 0; }
  html, body { width: 1200px; height: 1000px; overflow: hidden; background: var(--paper); }
  body { position: relative; font-family: "PT Sans", sans-serif; color: var(--ink); }

  .card { position: absolute; left: 338px; width: 589px; border: 1.5px solid var(--rule); background: var(--paper); overflow: hidden; }
  .card--front { top: 28px; height: 455px; }
  .card--back { top: 494px; height: 454px; }

  /* Front: cover */
  .cover { position: absolute; left: 0; top: 0; width: 342px; height: 100%; background: var(--night); overflow: hidden; }
  .cover__art { position: absolute; inset: 0;
    background:
      radial-gradient(ellipse 55% 45% at 50% 18%, #3a3a3a 0%, transparent 70%),
      radial-gradient(ellipse 45% 30% at 50% 42%, var(--skin) 0%, #2a1a12 60%, transparent 85%),
      radial-gradient(circle 175px at 50% 108%, var(--earth) 0%, #1c3a5c 55%, #0a1424 80%, transparent 82%),
      var(--night); }
  .cover__author { position: absolute; top: 22px; left: 0; width: 100%; text-align: center; font-family: "Questrial", sans-serif; font-size: 11px; letter-spacing: 12px; color: var(--author-grey); }

  .book-title { position: absolute; font-family: "Questrial", sans-serif; font-weight: 400; color: var(--title-white); line-height: 1; white-space: nowrap; }
  .book-title__main { display: block; }
  .book-title__sub { display: block; }

  .cover .book-title { left: 50px; top: 340px; }
  .cover .book-title__main { font-size: 62px; }
  .cover .book-title__sub { font-size: 25px; margin-top: 10px; margin-left: 2px; }

  /* Front: message */
  .message { position: absolute; left: 342px; top: 0; width: 247px; height: 100%; padding: 16px 28px 0 26px; }
  .message__lead { margin: 0 auto; width: 180px; text-align: center; font-family: "Arimo", sans-serif; font-weight: 700; font-size: 11px; line-height: 1.17; color: var(--headline-grey); }
  .message__lead-red { display: block; color: var(--accent-red); font-size: 13px; margin: 0 -10px; }
  .message__lead-dark { display: block; color: var(--ink); }
  .message__body { margin-top: 16px; font-size: 8.4px; line-height: 1.3; text-align: justify; }
  .message__body p { margin-bottom: 9px; }
  .message__body em { font-weight: 700; }

  .order-info { position: absolute; right: 28px; top: 320px; text-align: right; font-family: "Crimson Text", serif; font-size: 7.2px; line-height: 1.25; color: var(--ink); }
  .order-info p + p { margin-top: 7px; }

  .publisher-mark { position: absolute; right: 30px; top: 412px; display: flex; align-items: center; gap: 4px; font-family: "PT Sans", sans-serif; font-weight: 700; font-size: 8px; color: var(--ink); }
  .publisher-mark__dot { width: 7px; height: 7px; border-radius: 50%; background: var(--ink); }

  /* Back */
  .banner { position: absolute; left: 0; top: 0; width: 435px; height: 143px; background: var(--night); }
  .banner__art { position: absolute; left: 0; top: 0; width: 294px; height: 143px;
    background: radial-gradient(ellipse 95% 140% at 45% 20%, #3d6c9a 0%, var(--earth) 35%, #15304e 70%, var(--night) 100%); }
  .banner .book-title { left: 34px; top: 28px; }
  .banner .book-title__main { font-size: 56px; }
  .banner .book-title__sub { font-size: 23px; margin-top: 10px; }

  .stamp-box { position: absolute; left: 445px; top: 8px; width: 135px; height: 135px; border: 1.5px solid var(--rule); }
  .address-divider { position: absolute; left: 284px; top: 143px; width: 1.5px; height: 235px; background: var(--rule); }
</style>
</head>
<body>

<section class="card card--front">
  <div class="cover">
    <div class="cover__art" role="img" aria-label="Cover photo: hooded man's eyes looking over the planet Earth"></div>
    <p class="cover__author">RAY DOLVANE</p>
    <h1 class="book-title">
      <span class="book-title__main">The Devil</span>
      <span class="book-title__sub">in Modern Arcadia</span>
    </h1>
  </div>

  <div class="message">
    <p class="message__lead">There is a ferocious enemy in our world that's wreaking havoc in human culture.
      <span class="message__lead-red">His name is Satan (the Devil),</span>
      <span class="message__lead-dark">but millions of people don't believe that he exists.</span>
    </p>
    <div class="message__body">
      <p>Despite the widespread preaching of the gospel, only 4 in 10 (40%) American Christians believe that Satan exist. Those who believe think of him not as a real being but only as a symbol of evil.</p>
      <p>Satan is not only real but deeply entrenched in modern societies, harming us in ways that we can't possibly imagine.</p>
      <p>Discover how he influences people daily, regardless of their religious beliefs, for his purpose.</p>
      <p><em>The Devil in Modern Arcadia</em> not only exposes Satan's diabolical schemes in our world, but also shows how you can defend yourself against the most dangerous and aggressive personality in the universe and make it to heaven safely.</p>
    </div>
    <div class="order-info">
      <p>Available now from Northgate Press<br>www.northgatepress.example</p>
      <p>Order this title through your local bookseller<br>or preferred on-line retailer.<br>978-0-5550-1201-3 (SC ISBN)<br>978-0-5550-1202-0 (HC ISBN)<br>978-0-5550-1203-7 (Ebook ISBN)</p>
    </div>
    <div class="publisher-mark"><span class="publisher-mark__dot"></span>NORTHGATE PRESS</div>
  </div>
</section>

<section class="card card--back">
  <div class="banner">
    <div class="banner__art" role="img" aria-label="Photo of the planet Earth with clouds"></div>
    <div class="book-title">
      <span class="book-title__main">The Devil</span>
      <span class="book-title__sub">in Modern Arcadia</span>
    </div>
  </div>
  <div class="stamp-box"></div>
  <div class="address-divider"></div>
</section>

</body>
</html>
```